BrambleWare business card

Looking for business card design that supports our company/software values. We have 2 logo designs at the moment but open to change if you think you can enhance the brand. Check out website www.brambleware.com.au.

Target Market(s)

Education

Contact Information for Business Card

Name, title, mobile, email and website

Font styles to use
Sans Serif

Colors

Designer to choose colors to be used in the design.

Requirements
Must have
• BrambleWare logo with tree and tagline on rear side with dark grey background colour

```html
<!DOCTYPE html>
<html lang="en">
<head>
<meta charset="utf-8">
<title>BrambleWare Business Card</title>
<link rel="stylesheet" href="https://fonts.googleapis.com/css2?family=Montserrat:wght@300;400;500&display=swap">
<style>
  :root {
    --page-bg: #3a3a3a;
    --card-bg: #161616;
    --card-front-bg: #121212;
    --brand-green: #3db54a;
    --mark-grey: #9a9a9a;
    --mark-grey-light: #c9c9c9;
    --text-light: #e6e6e6;
    --text-muted: #bdbdbd;
  }
  * { box-sizing: border-box; margin: 0; padding: 0; }
  html, body { width: 1200px; height: 825px; overflow: hidden; }
  body {
    background: var(--page-bg);
    font-family: "Montserrat", sans-serif;
    position: relative;
  }
  .card {
    position: absolute;
    top: 258px;
    width: 540px;
    height: 309px;
    overflow: hidden;
    box-shadow: 0 12px 30px rgba(0,0,0,0.45);
  }
  /* Front side */
  .card-front {
    left: 40px;
    background: var(--card-front-bg);
    display: flex;
    align-items: center;
    justify-content: center;
  }
  .front-brand {
    display: flex;
    align-items: center;
    gap: 20px;
  }
  .front-dot {
    width: 64px; height: 64px;
    border-radius: 50%;
    background: var(--mark-grey);
    flex: none;
  }
  .front-name {
    font-size: 42px;
    font-weight: 400;
    color: var(--mark-grey-light);
    letter-spacing: 0.5px;
    white-space: nowrap;
  }
  /* Back side */
  .card-back { left: 620px; background: var(--card-bg); }
  .brand-block {
    position: absolute;
    right: 44px; top: 52px;
    display: flex; align-items: center; gap: 12px;
  }
  .brand-dot {
    width: 40px; height: 40px; border-radius: 50%;
    background: var(--brand-green);
  }
  .brand-text { display: flex; flex-direction: column; }
  .brand-name {
    font-size: 26px; font-weight: 500; color: var(--text-light);
    padding-bottom: 3px;
    border-bottom: 1px solid var(--text-muted);
  }
  .brand-tagline {
    font-size: 10.5px; font-weight: 400; color: var(--text-muted);
    padding-top: 3px; letter-spacing: 0.3px;
  }
  .person {
    position: absolute;
    right: 290px; top: 150px;
    text-align: right;
  }
  .person-name {
    font-size: 23px; font-weight: 300; color: var(--text-light);
    white-space: nowrap;
  }
  .person-title {
    margin-top: 4px;
    font-size: 10px; font-weight: 400; color: var(--brand-green);
    letter-spacing: 1px; text-transform: uppercase;
  }
  .divider {
    position: absolute;
    left: 270px; top: 150px;
    width: 1px; height: 90px;
    background: var(--brand-green);
  }
  .contact-list {
    position: absolute;
    left: 290px; top: 160px;
    list-style: none;
  }
  .contact-item {
    display: flex; align-items: center; gap: 10px;
    font-size: 12.5px; color: var(--text-light);
    height: 24px;
    white-space: nowrap;
  }
  .contact-icon { width: 12px; height: 12px; flex: none; }
  .green-band {
    position: absolute;
    left: 0; right: 0; bottom: 0;
    height: 26px;
    background: var(--brand-green);
  }
</style>
</head>
<body>
  <section class="card card-front" aria-label="Card front">
    <div class="front-brand">
      <div class="front-dot"></div>
      <div class="front-name">BrambleWare</div>
    </div>
  </section>

  <section class="card card-back" aria-label="Card back">
    <div class="brand-block">
      <div class="brand-dot"></div>
      <div class="brand-text">
        <span class="brand-name">BrambleWare</span>
        <span class="brand-tagline">Student Success Platform</span>
      </div>
    </div>

    <div class="person">
      <div class="person-name">Daniel Brookfield</div>
      <div class="person-title">Job Title</div>
    </div>

    <div class="divider"></div>

    <ul class="contact-list">
      <li class="contact-item">
        <svg class="contact-icon" viewBox="0 0 24 24" aria-hidden="true"><path fill="#3db54a" d="M6.6 10.8a15.1 15.1 0 0 0 6.6 6.6l2.2-2.2c.3-.3.7-.4 1-.2 1.1.4 2.3.6 3.6.6.6 0 1 .4 1 1V20c0 .6-.4 1-1 1A17 17 0 0 1 3 4c0-.6.4-1 1-1h3.5c.6 0 1 .4 1 1 0 1.3.2 2.5.6 3.6.1.3 0 .7-.2 1z"/></svg>
        <span>000 000 0000</span>
      </li>
      <li class="contact-item">
        <svg class="contact-icon" viewBox="0 0 24 24" aria-hidden="true"><rect x="2" y="5" width="20" height="14" rx="1.5" fill="#3db54a"/><path d="M3 6l9 7 9-7" fill="none" stroke="#161616" stroke-width="2"/></svg>
        <span>name@brambleware.com.au</span>
      </li>
      <li class="contact-item">
        <svg class="contact-icon" viewBox="0 0 24 24" aria-hidden="true"><g fill="none" stroke="#3db54a" stroke-width="2"><circle cx="12" cy="12" r="9.5"/><ellipse cx="12" cy="12" rx="4" ry="9.5"/><path d="M2.5 12h19"/></g></svg>
        <span>www.brambleware.com.au</span>
      </li>
    </ul>

    <div class="green-band"></div>
  </section>
</body>
</html>
```